TM Estates - Stone Hof Design

Looking for a double sides design, 1 side for my realestate and the other for home building. ( TM Estates on 1 side, Stone Hof card on the other Side
Side 1 - Priya Mond ~ Vex Realty logo and Company ( the Real estate district )
Priya Mond
Priya@Priyamondhomes.example
IG - Priya_Nwt_Agent
FB - priyam
Cell - 5550193847
3874 46 St Nw

Side 2
Priya Mond
5550193847
IG - Stonehof_Nwt
Stonehofbuild@mailbox.example

Target Market(s)

Home buyers/ sellers

Industry/Entity Type

Home builders - Realestate

Contact Information for Business Card

Above

Requirements
Must have
• Black OR White background - my information -

```html
<!DOCTYPE html>
<html lang="en">
<head>
<meta charset="utf-8">
<title>Priya Mond – Business Cards</title>
<link rel="stylesheet" href="https://fonts.googleapis.com/css2?family=Cinzel:wght@400;600&family=Tinos&display=swap">
<style>
  :root {
    --bg: #2b2b2b;
    --card: #1f1f20;
    --card-shadow: rgba(0,0,0,0.55);
    --ink: #ffffff;
    --accent: #1f7ad0;
    --emboss: #2a2a2c;
    --badge: #d9d9d9;
  }
  * { box-sizing: border-box; margin: 0; padding: 0; }
  html, body { width: 1200px; height: 900px; overflow: hidden; background: var(--bg); }
  .canvas { position: relative; width: 1200px; height: 900px; }

  .card {
    position: absolute; width: 580px; height: 330px;
    background: var(--card); border-radius: 22px;
    box-shadow: 0 14px 30px var(--card-shadow);
    color: var(--ink); overflow: hidden;
  }
  .card--builder { left: 70px; top: 80px; }
  .card--realty  { left: 550px; top: 490px; }

  .holder-name {
    position: absolute; left: 42px;
    font-family: "Cinzel", serif; font-weight: 400; font-size: 32px; letter-spacing: 1px;
  }
  .holder-rule { position: absolute; left: 42px; width: 26px; height: 3px; background: var(--accent); }

  .contact-list { position: absolute; left: 42px; list-style: none;
    font-family: "Tinos", serif; font-size: 15px; line-height: 21px; }
  .contact-list li { display: flex; align-items: center; gap: 10px; }
  .contact-list svg { width: 13px; height: 13px; flex: none; fill: var(--accent); }

  .brand-name { position: absolute; font-family: "Cinzel", serif; font-weight: 600; display: flex; align-items: center; gap: 10px; }
  .brand-mark { width: 14px; height: 14px; background: currentColor; }
  .brand-faint { position: absolute; font-family: "Cinzel", serif; font-weight: 600; color: var(--emboss); }

  .card--builder .brand-name { right: 44px; top: 40px; font-size: 36px; color: var(--ink); }
  .card--builder .brand-faint { right: 30px; top: 120px; font-size: 62px; }
  .card--builder .holder-name { top: 178px; }
  .card--builder .holder-rule { top: 222px; }
  .card--builder .contact-list { top: 232px; }

  .card--realty .brand-name { right: 44px; top: 36px; font-size: 38px; color: var(--accent); }
  .card--realty .brand-faint { right: 26px; top: 110px; font-size: 66px; }
  .card--realty .holder-name { top: 132px; }
  .card--realty .holder-rule { top: 176px; }
  .card--realty .contact-list { top: 184px; }

  .partner-row { position: absolute; right: 40px; bottom: 40px; display: flex; align-items: center; gap: 18px; }
  .partner-badge { width: 76px; height: 30px; background: var(--badge); border-radius: 3px; }
  .partner-realty { font-family: "Cinzel", serif; font-size: 15px; color: var(--ink); display: flex; align-items: center; gap: 6px; }
  .partner-dot { width: 12px; height: 12px; border-radius: 50%; background: var(--ink); }
</style>
</head>
<body>
<main class="canvas">

  <section class="card card--builder" aria-label="Stone Hof business card">
    <div class="brand-name"><span class="brand-mark"></span>Stone Hof</div>
    <div class="brand-faint" aria-hidden="true">Stone Hof</div>
    <h1 class="holder-name">Priya Mond</h1>
    <div class="holder-rule"></div>
    <ul class="contact-list">
      <li><svg viewBox="0 0 16 16"><path d="M3 1h3l1.5 4-2 1.2a9 9 0 0 0 4.3 4.3L11 8.5l4 1.5v3a2 2 0 0 1-2 2A12 12 0 0 1 1 3a2 2 0 0 1 2-2z"/></svg>5550193847</li>
      <li><svg viewBox="0 0 16 16"><path d="M1 3h14v10H1z M1 3l7 6 7-6" stroke="#1f1f20" stroke-width="1.2"/></svg>Stonehofbuild@mailbox.example</li>
      <li><svg viewBox="0 0 16 16"><circle cx="8" cy="8" r="7"/><path d="M1 8h14M8 1c-3 4-3 10 0 14M8 1c3 4 3 10 0 14" stroke="#1f1f20" fill="none"/></svg>www.stonehofbuild.example</li>
      <li><svg viewBox="0 0 16 16"><circle cx="8" cy="8" r="7"/></svg>Stonehof_Nwt</li>
    </ul>
  </section>

  <section class="card card--realty" aria-label="TM Estates business card">
    <div class="brand-name"><span class="brand-mark"></span>TM Estates</div>
    <div class="brand-faint" aria-hidden="true">TM Estates</div>
    <h1 class="holder-name">Priya Mond</h1>
    <div class="holder-rule"></div>
    <ul class="contact-list">
      <li><svg viewBox="0 0 16 16"><path d="M3 1h3l1.5 4-2 1.2a9 9 0 0 0 4.3 4.3L11 8.5l4 1.5v3a2 2 0 0 1-2 2A12 12 0 0 1 1 3a2 2 0 0 1 2-2z"/></svg>5550193847</li>
      <li><svg viewBox="0 0 16 16"><path d="M1 3h14v10H1z M1 3l7 6 7-6" stroke="#1f1f20" stroke-width="1.2"/></svg>Priya@Priyamondhomes.example</li>
      <li><svg viewBox="0 0 16 16"><circle cx="8" cy="8" r="7"/><path d="M1 8h14M8 1c-3 4-3 10 0 14M8 1c3 4 3 10 0 14" stroke="#1f1f20" fill="none"/></svg>www.priyamondhomes.example</li>
      <li><svg viewBox="0 0 16 16"><path d="M8 1a5 5 0 0 1 5 5c0 4-5 9-5 9S3 10 3 6a5 5 0 0 1 5-5z"/><circle cx="8" cy="6" r="2" fill="#1f1f20"/></svg>3874 46 St Nw</li>
      <li><svg viewBox="0 0 16 16"><circle cx="8" cy="8" r="7"/></svg>Priya_Nwt_Agent</li>
      <li><svg viewBox="0 0 16 16"><rect x="1" y="1" width="14" height="14" rx="2"/></svg>priyam</li>
    </ul>
    <div class="partner-row">
      <div class="partner-badge" aria-label="Partner badge"></div>
      <div class="partner-realty"><span class="partner-dot"></span>Vex Realty</div>
    </div>
  </section>

</main>
</body>
</html>
```